Want to incorporate elements of all these items to make an amazing sign to welcome people to the community. The sign is 6x4 and needs to incorporate the following items:

Welcome to Thistle Grove

Come visit the DWR sales center at 548 marlow road
High Speed Fiber Internet
Land financing starting at $299 (No credit checks)
Let us build your dream home!
517-384-2296
We like the gold and black design no teal or blue that was another agents design. Some combination of the current sign all the stuff listed above and then design elements that tie into the truck wrap.

Target Market(s)

People visiting the neighborhood

Industry/Entity Type

real estate and construction

Font styles to use
Serif

Colors

Designer to choose colors to be used in the design.

Requirements
Must have
• DWR Home Builders Welcomes you to Thistle Grove, Let us build your dream home, Phone number, Land financing starting at $299 NO credit checks

```html
<!DOCTYPE html>
<html lang="en">
<head>
<meta charset="utf-8">
<title>Welcome to Thistle Grove</title>
<link rel="stylesheet" href="https://fonts.googleapis.com/css2?family=Cinzel:wght@600;700&family=Gelasio:wght@700&family=Jost:wght@500;600&display=swap">
<style>
  :root {
    --ink: #000000;
    --gold: #d9a82b;
    --gold-light: #f3d36a;
    --gold-deep: #9c7212;
    --gold-dim: #3a2c0c;
  }
  html, body {
    margin: 0;
    padding: 0;
    width: 1200px;
    height: 800px;
    overflow: hidden;
    background: var(--ink);
  }
  .sign {
    display: block;
    width: 1200px;
    height: 800px;
  }
  .serif-caps { font-family: "Cinzel", "Times New Roman", serif; font-weight: 700; }
  .serif-text { font-family: "Gelasio", Georgia, serif; font-weight: 700; }
  .sans-text  { font-family: "Jost", "Helvetica Neue", sans-serif; font-weight: 600; }
  .gold-text { fill: url(#goldFill); filter: url(#emboss); }
  .welcome { font-size: 31px; letter-spacing: 5px; font-weight: 600; }
  .community-name { font-size: 94px; letter-spacing: 2px; }
  .visit-line { font-size: 34px; }
  .address { font-size: 80px; letter-spacing: 4px; }
  .feature { font-size: 31px; font-weight: 500; }
  .feature-note { font-size: 20px; font-weight: 500; }
  .tagline { font-size: 45px; word-spacing: 12px; letter-spacing: 1px; }
  .phone { font-size: 122px; }
  .rule { stroke: var(--gold); stroke-width: 2; }
  .frame { fill: none; stroke: url(#goldLine); stroke-width: 4; }
  .ornament-area { fill: url(#ornamentTone); }
</style>
</head>
<body>
<svg class="sign" viewBox="0 0 1200 800" xmlns="http://www.w3.org/2000/svg">
  <defs>
    <linearGradient id="goldFill" x1="0" y1="0" x2="0" y2="1">
      <stop offset="0" stop-color="#f0c94e"/>
      <stop offset="0.55" stop-color="#d9a82b"/>
      <stop offset="1" stop-color="#b8861a"/>
    </linearGradient>
    <linearGradient id="goldLine" x1="0" y1="0" x2="1" y2="1">
      <stop offset="0" stop-color="#c8961f"/>
      <stop offset="0.5" stop-color="#f3d36a"/>
      <stop offset="1" stop-color="#c8961f"/>
    </linearGradient>
    <radialGradient id="ornamentTone" cx="0.5" cy="0.5" r="0.6">
      <stop offset="0" stop-color="#4a3810"/>
      <stop offset="1" stop-color="#1a1405"/>
    </radialGradient>
    <filter id="emboss" x="-5%" y="-10%" width="110%" height="130%">
      <feDropShadow dx="1.5" dy="2" stdDeviation="0.8" flood-color="#000" flood-opacity="0.85"/>
    </filter>
  </defs>

  <rect class="backdrop" width="1200" height="800" fill="var(--ink)"/>
  <rect class="frame" x="30" y="31" width="1142" height="739"/>

  <!-- corner flourishes -->
  <rect class="ornament-area" x="51" y="51" width="156" height="156" role="img" aria-label="Gold scroll flourish, top left corner"/>
  <rect class="ornament-area" x="993" y="51" width="156" height="156" role="img" aria-label="Gold scroll flourish, top right corner"/>
  <rect class="ornament-area" x="51" y="590" width="156" height="160" role="img" aria-label="Gold scroll flourish, bottom left corner"/>
  <rect class="ornament-area" x="993" y="590" width="156" height="160" role="img" aria-label="Gold scroll flourish, bottom right corner"/>

  <!-- title header -->
  <rect class="ornament-area" x="419" y="59" width="359" height="41" role="img" aria-label="Gold scrollwork crest above the welcome line"/>
  <text class="serif-caps gold-text welcome" x="601" y="141" text-anchor="middle">WELCOME TO</text>
  <text class="serif-caps gold-text community-name" x="600" y="228" text-anchor="middle">THISTLE GROVE</text>
  <line class="rule" x1="140" y1="245" x2="1057" y2="245"/>
  <line class="rule" x1="150" y1="253" x2="1047" y2="253"/>
  <rect class="ornament-area" x="474" y="240" width="255" height="22" role="img" aria-label="Gold scrollwork divider below the community name"/>

  <!-- sales center -->
  <text class="sans-text gold-text visit-line" x="601" y="324" text-anchor="middle">COME VISIT THE DWR SALES CENTER AT</text>
  <text class="serif-caps gold-text address" x="600" y="404" text-anchor="middle">548 MARLOW ROAD</text>

  <!-- features -->
  <line class="rule" x1="269" y1="434" x2="930" y2="434"/>
  <text class="sans-text gold-text feature" x="600" y="473" text-anchor="middle">High-Speed Fiber Internet</text>
  <line class="rule" x1="269" y1="495" x2="930" y2="495"/>
  <text class="sans-text gold-text feature" x="600" y="529" text-anchor="middle">Land Financing from $299 <tspan class="feature-note">(No Credit Checks!)</tspan></text>
  <line class="rule" x1="269" y1="549" x2="930" y2="549"/>

  <!-- call to action -->
  <text class="serif-text gold-text tagline" x="597" y="604" text-anchor="middle">Let Us Build Your Dream Home!</text>
  <text class="serif-text gold-text phone" x="612" y="711" text-anchor="middle">517-384-2296</text>
</svg>
</body>
</html>
```